Business card for Autism Consultancy

I need a double-sided business card for Brightpath Learning Consultancy
Please try to use the colours and graphics in line with our website www.brightpathlearn.nz
Front side
Logo and the name of the company – Brightpath Learning Consultancy
We use Child-Centred, Modern and Innovative approaches
Teaching autistic children to bond, laugh and play
www.brightpathlearn.nz
info@brightpathlearn.nz
phone +64 09 37 615 48
Back side
Photo
Mirela Dunstan
Founder
Postgraduate Autism (Children) Specialist (with Merit)
Qualified by the Faculty of Learning Support and Access Studies (FLSA), Harwell Vale University
mirela@brightpathlearn.nz
phone +64 937 615 48
mobile: +64 20 6283 9150
Please do not convert the text fields to outlines, i.e. I need to be able to edit any text after.
The final design should be either in Adobe Illustrator or Adobe Photoshop format.
The Specs for the business card are:
Full Bleed Size
94 x 58 mm
1110 x 685 pixels
Document Trim Size
91 x 55 mm
1075 x 650 pixels

```html
<!DOCTYPE html>
<html lang="en">
<head>
<meta charset="utf-8">
<title>Brightpath Learning Consultancy – Business Card</title>
<link rel="stylesheet" href="https://fonts.googleapis.com/css2?family=Nunito:wght@400;600;700;800&display=swap">
<style>
  :root {
    --navy: #2b3a7a;
    --teal: #38b1ab;
    --yellow: #f3c500;
    --white: #ffffff;
    --ink: #1d1d1d;
    --page: #e9e9e6;
  }
  * { margin: 0; padding: 0; box-sizing: border-box; }
  html, body { width: 1200px; height: 1200px; overflow: hidden; }
  body {
    background: var(--page);
    font-family: "Nunito", sans-serif;
    position: relative;
  }
  .card {
    position: absolute;
    left: 237px;
    width: 722px;
    height: 435px;
    overflow: hidden;
    box-shadow: 0 6px 18px rgba(0,0,0,0.18);
  }
  .card--front { top: 104px; background: var(--white); }
  .card--back { top: 627px; background: var(--yellow); }

  /* Front */
  .brand-mark {
    position: absolute; left: 100px; top: 50px;
    width: 140px; height: 140px; border-radius: 50%;
    background: var(--yellow);
  }
  .brand-name {
    position: absolute; right: 76px; top: 52px;
    text-align: right;
    color: var(--navy);
    font-weight: 800;
    font-size: 38px;
    line-height: 1.15;
  }
  .tagline {
    position: absolute; left: 0; right: 0; top: 229px;
    text-align: center;
    color: var(--teal);
    font-weight: 700;
    font-size: 20px;
    line-height: 31px;
  }
  .band-rule {
    position: absolute; left: 0; right: 0; top: 323px; height: 8px;
    background: var(--yellow);
  }
  .band {
    position: absolute; left: 0; right: 0; top: 329px; bottom: 0;
    background: var(--teal);
  }
  .contact-icon {
    position: absolute; top: 305px;
    width: 50px; height: 50px; border-radius: 50%;
    background: var(--yellow);
    border: 3px solid var(--teal);
    display: flex; align-items: center; justify-content: center;
  }
  .contact-icon svg { width: 28px; height: 28px; }
  .contact-text {
    position: absolute; top: 366px; width: 230px;
    text-align: center;
    color: var(--white);
    font-weight: 600;
    font-size: 15.5px;
    letter-spacing: 0.3px;
  }
  .divider {
    position: absolute; top: 357px; width: 2px; height: 54px;
    background: var(--white);
  }

  /* Back */
  .portrait {
    position: absolute; left: 261px; top: 22px;
    width: 200px; height: 200px; border-radius: 50%;
    border: 4px solid var(--white);
    background: radial-gradient(circle at 50% 42%, #d9a58a 0%, #9c6a52 45%, #4a3a36 100%);
  }
  .name-pill {
    position: absolute; left: 196px; top: 224px;
    width: 330px; height: 45px;
    background: var(--white);
    border: 2px solid var(--teal);
    border-radius: 22px;
    display: flex; align-items: center; justify-content: center;
    color: var(--teal);
    font-weight: 800;
    font-size: 26px;
    letter-spacing: 0.8px;
  }
  .role {
    position: absolute; left: 0; right: 0; top: 276px;
    text-align: center;
    color: var(--ink);
    font-weight: 600;
    font-size: 14px;
    letter-spacing: 0.4px;
  }
  .credentials {
    position: absolute; left: 0; right: 0; top: 300px; height: 74px;
    background: var(--white);
    display: flex; align-items: center; justify-content: center;
    text-align: center;
    color: var(--teal);
    font-weight: 600;
    font-size: 16px;
    line-height: 25px;
  }
  .credentials small { font-size: 13px; }
  .direct {
    position: absolute; top: 380px;
    display: flex; align-items: center; gap: 7px;
    color: var(--ink);
    font-weight: 600;
    font-size: 16.5px;
    letter-spacing: 0.3px;
  }
  .direct-icon {
    width: 22px; height: 22px; border-radius: 4px;
    background: var(--ink);
    display: flex; align-items: center; justify-content: center;
  }
  .direct-icon svg { width: 15px; height: 15px; }
</style>
</head>
<body>

<section class="card card--front">
  <div class="brand-mark"></div>
  <div class="brand-name">Brightpath Learning<br>Consultancy</div>

  <p class="tagline">We use Child-Centred, Modern and Innovative approaches,<br>Teaching autistic children to bond, Laugh and play</p>

  <div class="band-rule"></div>
  <div class="band"></div>

  <div class="contact-icon" style="left:89px">
    <svg viewBox="0 0 24 24" fill="none" stroke="#2b3a7a" stroke-width="1.6" stroke-linejoin="round">
      <path d="M6 3l3 0 1.5 4-2 1.5a11 11 0 0 0 7 7l1.5-2 4 1.5v3a2 2 0 0 1-2 2A17 17 0 0 1 4 5a2 2 0 0 1 2-2z"/>
      <path d="M14 4a6 6 0 0 1 6 6M14 7.5a3 3 0 0 1 2.5 2.5"/>
    </svg>
  </div>
  <div class="contact-icon" style="left:310px">
    <svg viewBox="0 0 24 24" fill="none" stroke="#2b3a7a" stroke-width="1.5">
      <circle cx="12" cy="12" r="9.5"/>
      <path d="M3 9.5h18M3 14.5h18"/>
      <text x="12" y="13.7" font-size="5" text-anchor="middle" fill="#2b3a7a" stroke="none" font-family="Nunito, sans-serif" font-weight="800">www</text>
    </svg>
  </div>
  <div class="contact-icon" style="left:559px">
    <svg viewBox="0 0 24 24" fill="none" stroke="#2b3a7a" stroke-width="1.5" stroke-linejoin="round">
      <path d="M3 10l9-6 9 6v10H3z"/>
      <path d="M3 10l9 6 9-6M3 20l7-5M21 20l-7-5"/>
      <circle cx="12" cy="9" r="2"/>
    </svg>
  </div>

  <div class="contact-text" style="left:0">+64 09 37 615 48</div>
  <div class="divider" style="left:212px"></div>
  <div class="contact-text" style="left:221px">www.brightpathlearn.nz</div>
  <div class="divider" style="left:460px"></div>
  <div class="contact-text" style="left:469px">info@brightpathlearn.nz</div>
</section>

<section class="card card--back">
  <div class="portrait" role="img" aria-label="Portrait photo of Mirela Dunstan, founder"></div>
  <div class="name-pill">MIRELA DUNSTAN</div>
  <p class="role">FOUNDER</p>
  <p class="credentials">
    <span>Postgraduate Autism <small>(Children)</small> Specialist <small>(with Merit)</small>&nbsp; Qualified by the Faculty of<br>Learning Support and Access Studies <small>(FLSA)</small>, Harwell Vale University</span>
  </p>

  <div class="direct" style="left:29px">
    <span class="direct-icon">
      <svg viewBox="0 0 24 24" fill="none" stroke="#fff" stroke-width="2" stroke-linejoin="round"><path d="M3 6h18v12H3z"/><path d="M3 6l9 7 9-7"/></svg>
    </span>
    mirela@brightpathlearn.nz
  </div>
  <div class="direct" style="left:324px">
    <span class="direct-icon">
      <svg viewBox="0 0 24 24" fill="none" stroke="#fff" stroke-width="2" stroke-linejoin="round"><path d="M6 3h3l1.5 4-2 1.5a11 11 0 0 0 7 7l1.5-2 4 1.5v3a2 2 0 0 1-2 2A17 17 0 0 1 4 5a2 2 0 0 1 2-2z"/></svg>
    </span>
    +64 937 615 48
  </div>
  <div class="direct" style="left:521px">
    <span class="direct-icon">
      <svg viewBox="0 0 24 24" fill="none" stroke="#fff" stroke-width="2" stroke-linejoin="round"><rect x="7" y="2" width="10" height="20" rx="2"/><path d="M11 18h2"/></svg>
    </span>
    +64 20 6283 9150
  </div>
</section>

</body>
</html>
```